Author of book needs a Facebook page to route possible customers to the books website.

I need a Facebook page to promote my new book: Walking Tall Alone-A Practical Safety Handbook For Ladies-Revised. Idealy the Facebook page must include a picture of the book, an author bio and a short paragraph or two about the book. All of this can be obtained at the books website at www.brightwardcounsel.example. Since I am expecting a high volume of visitors I need the Facebook page to be "Liked" rather than "Friends."

Target Market(s)

Women of all ages

Font styles to use
Sans Serif

Colors

Designer to choose colors to be used in the design.

Requirements
Must have
• Link to the www.brightwardcounsel.example website. Picture of the book cover. Author bio.

```html
<!DOCTYPE html>
<html lang="en">
<head>
<meta charset="utf-8">
<title>Walking Tall Alone – Marcus Dellane</title>
<link rel="stylesheet" href="https://fonts.googleapis.com/css2?family=Open+Sans:ital,wght@0,400;0,700;0,800;1,700&display=swap">
<style>
  :root {
    --bg: #ffffff;
    --ink: #111111;
    --accent: #f58a1f;
    --subtitle: #666666;
    --bio: #b3b3b3;
    --cover-dark: #141414;
    --cover-mid: #2c2c2c;
  }
  * { margin: 0; padding: 0; box-sizing: border-box; }
  html, body {
    width: 1200px;
    height: 458px;
    overflow: hidden;
    background: var(--bg);
  }
  .banner {
    position: relative;
    width: 1200px;
    height: 458px;
    background: var(--bg);
    font-family: "Open Sans", sans-serif;
  }
  .book-cover {
    position: absolute;
    left: 30px;
    top: 8px;
    width: 340px;
    height: 442px;
    border-radius: 4px 10px 10px 4px;
    background: linear-gradient(100deg, var(--cover-mid) 0%, var(--cover-dark) 12%, var(--cover-dark) 86%, #222222 100%);
    box-shadow: 8px 10px 18px rgba(0,0,0,0.25);
  }
  .headline {
    position: absolute;
    left: 426px;
    width: 720px;
    text-align: center;
    white-space: nowrap;
  }
  .author-name {
    top: 28px;
    font-size: 40px;
    font-weight: 800;
    color: var(--ink);
    letter-spacing: 0.5px;
    line-height: 48px;
  }
  .author-rule {
    position: absolute;
    left: 716px;
    top: 90px;
    width: 140px;
    height: 3px;
    background: var(--accent);
  }
  .book-title {
    top: 126px;
    font-size: 50px;
    font-weight: 700;
    color: var(--ink);
    line-height: 60px;
  }
  .book-subtitle {
    top: 180px;
    font-size: 25px;
    font-weight: 700;
    color: var(--subtitle);
    line-height: 32px;
  }
  .book-link {
    top: 228px;
    font-size: 30px;
    font-weight: 700;
    font-style: italic;
    color: var(--accent);
    text-decoration: none;
    line-height: 40px;
  }
  .author-bio {
    position: absolute;
    left: 478px;
    top: 300px;
    width: 720px;
    font-size: 15.5px;
    line-height: 24px;
    color: var(--bio);
    text-align: center;
  }
</style>
</head>
<body>
  <main class="banner">
    <div class="book-cover" role="img" aria-label="3D render of the black book cover of Walking Tall Alone by Marcus Dellane"></div>
    <h2 class="headline author-name">MARCUS DELLANE</h2>
    <div class="author-rule"></div>
    <h1 class="headline book-title">Walking Tall Alone</h1>
    <p class="headline book-subtitle">A Practical Safety Handbook For Ladies Revised</p>
    <a class="headline book-link" href="http://www.brightwardcounsel.example/">http://www.brightwardcounsel.example/</a>
    <p class="author-bio">Marcus Dellane is a former security consultant whose long field career includes threat assessment work and close protection assignments across North America, Europe and the Pacific. Years spent training security teams, advising solo travelers and teaching personal safety courses to women of every age shaped the practical and calm approach found in this handbook...</p>
  </main>
</body>
</html>
```